TALRENO Business Cards

We require a business card for our company that provides IT consulting services. We already have a logo that needs to be used on the card. We want a clean professional looking design that incorporates our colours. Our main focus is providing managed services to business, which involves us looking after all of their IT requirements including managing servers/networks, projects, and procurement.

Industry/Entity Type

Information Technology

Requirements
Must have
• our logo, contact information, name, title, phone numbers

```html
<!DOCTYPE html>
<html lang="en">
<head>
<meta charset="utf-8">
<title>TALRENO Business Card</title>
<link rel="stylesheet" href="https://fonts.googleapis.com/css2?family=Source+Sans+3:wght@400;600;700&display=swap">
<style>
  :root {
    --brand-blue: #0a93d0;
    --card-white: #ffffff;
    --page-bg: #e9ecef;
    --text-light: #ffffff;
  }
  * { margin: 0; padding: 0; box-sizing: border-box; }
  html, body {
    width: 1200px;
    height: 900px;
    overflow: hidden;
    background: var(--page-bg);
    font-family: "Source Sans 3", sans-serif;
  }
  .business-card {
    position: absolute;
    left: 80px;
    top: 128px;
    width: 1040px;
    height: 643px;
    background: var(--card-white);
    overflow: hidden;
    box-shadow: 0 10px 30px rgba(0,0,0,0.12);
  }
  .card-background {
    position: absolute;
    inset: 0;
  }
  .social-row {
    position: absolute;
    left: 58px;
    top: 80px;
    display: flex;
    gap: 11px;
  }
  .social-dot {
    width: 38px;
    height: 38px;
    border-radius: 50%;
    background: var(--text-light);
  }
  .contact-list {
    position: absolute;
    left: 64px;
    top: 285px;
    color: var(--text-light);
    font-size: 28px;
    line-height: 38px;
    font-weight: 400;
  }
  .contact-line {
    display: flex;
    align-items: center;
    gap: 7px;
  }
  .contact-icon {
    width: 22px;
    height: 22px;
    flex: none;
  }
  .address {
    margin-top: 14px;
    line-height: 39px;
  }
  .person {
    position: absolute;
    left: 66px;
    top: 518px;
    color: var(--text-light);
  }
  .person-name {
    font-size: 35px;
    font-weight: 700;
    letter-spacing: 0.5px;
    line-height: 40px;
  }
  .person-title {
    font-size: 28px;
    font-weight: 400;
    line-height: 34px;
  }
  .brand-name {
    position: absolute;
    left: 520px;
    width: 450px;
    top: 380px;
    text-align: center;
    color: var(--brand-blue);
    font-size: 96px;
    font-weight: 600;
    letter-spacing: 6px;
    line-height: 110px;
  }
</style>
</head>
<body>
  <div class="business-card">
    <svg class="card-background" width="1040" height="643" viewBox="0 0 1040 643" aria-hidden="true">
      <path d="M0 0 H678 C560 60 420 100 400 200 C388 400 520 560 654 643 H0 Z" fill="var(--brand-blue)"/>
    </svg>

    <div class="social-row" aria-label="Social profiles">
      <span class="social-dot"></span>
      <span class="social-dot"></span>
      <span class="social-dot"></span>
      <span class="social-dot"></span>
      <span class="social-dot"></span>
    </div>

    <div class="contact-list">
      <div class="contact-line">
        <svg class="contact-icon" viewBox="0 0 24 24" aria-hidden="true">
          <path d="M6.6 10.8a15.1 15.1 0 0 0 6.6 6.6l2.2-2.2a1 1 0 0 1 1-.25 11.4 11.4 0 0 0 3.6.57 1 1 0 0 1 1 1V20a1 1 0 0 1-1 1A17 17 0 0 1 3 4a1 1 0 0 1 1-1h3.5a1 1 0 0 1 1 1c0 1.25.2 2.45.57 3.57a1 1 0 0 1-.25 1z" fill="#fff"/>
        </svg>
        <span>403-555-0182</span>
      </div>
      <div class="contact-line">
        <svg class="contact-icon" viewBox="0 0 24 24" aria-hidden="true">
          <rect x="2" y="5" width="20" height="14" fill="#fff"/>
          <path d="M2 5 L12 13 L22 5" fill="none" stroke="var(--brand-blue)" stroke-width="2"/>
        </svg>
        <span>info@talreno.com</span>
      </div>
      <div class="contact-line">
        <svg class="contact-icon" viewBox="0 0 24 24" aria-hidden="true">
          <circle cx="12" cy="12" r="10" fill="#fff"/>
          <path d="M2 12 H22 M12 2 C7 7 7 17 12 22 M12 2 C17 7 17 17 12 22" fill="none" stroke="var(--brand-blue)" stroke-width="1.5"/>
        </svg>
        <span>www.talreno.com</span>
      </div>
      <div class="address">
        418 Centre Avenue<br>
        Box 2714, Red Ridge, AB
      </div>
    </div>

    <div class="person">
      <div class="person-name">DANIEL HARWICK</div>
      <div class="person-title">President &amp; Technology Consultant</div>
    </div>

    <div class="brand-name">TALRENO</div>
  </div>
</body>
</html>
```